1912 Zur Glutpfanne Website
Zielgruppe
Wir betreiben ein Hamburger-Restaurant. Alle Zutaten kommen wenn möglich, aus der Region. Wir benutzen keine Farb- und Konservierungsstoffe. Unser Fleisch ist ein frisches Bio-Rinderhack. Das Brot backen wir selber und die Saucen sind nach eigener Rezeptur hausgemacht. Der Käse wird in einem Familienbetrieb frisch für uns hergestellt. Jeder Gast kann sich seinen Burger frisch nach seinen Wünschen zusammenstellen und bei der Zubereitung zuschauen. Essen mit Herkunft aus Tradition!
Aufgabenstellung
Ansprechendes Design, welches unsere Philosophie und die Liebe zum Burger widerspiegelt. Frische Zutaten in wechselnden Slide-Shows, Wertschätzung der Rohprodukte und den Genuss beim Essen.

```html
<!DOCTYPE html>
<html lang="de">
<head>
<meta charset="utf-8">
<title>1912 Zur Glutpfanne</title>
<link rel="stylesheet" href="https://fonts.googleapis.com/css2?family=Signika:wght@300;400;600&family=Kalam:wght@400&display=swap">
<style>
  :root {
    --wood-dark: #2e1306;
    --wood-mid: #4a200c;
    --green: #6cc300;
    --green-dark: #4fa200;
    --green-light: #86d80f;
    --orange: #f07d00;
    --text: #1c1c1c;
    --white: #ffffff;
    --chalk: #2b2b2b;
  }
  * { margin: 0; padding: 0; box-sizing: border-box; }
  html, body { width: 1200px; height: 988px; overflow: hidden; }
  body {
    position: relative;
    font-family: "Signika", sans-serif;
    font-weight: 300;
    color: var(--text);
    background: linear-gradient(90deg, var(--wood-dark) 0%, var(--wood-mid) 20%, #3a1808 45%, var(--wood-mid) 70%, var(--wood-dark) 100%);
  }
  .wood-backdrop { position: absolute; inset: 0; }
  .hero-photo {
    position: absolute; left: 300px; top: 0; width: 780px; height: 217px;
    background: linear-gradient(100deg, #f3eee4 0%, #9dbb4a 22%, #d9442a 45%, #f0e6c8 60%, #7a3a1a 80%, #efe9de 100%);
  }
  .nav-band {
    position: absolute; left: 0; top: 217px; width: 1200px; height: 49px;
    background: linear-gradient(180deg, var(--green-light) 0%, var(--green) 55%, var(--green-dark) 100%);
  }
  .main-nav { position: absolute; left: 0; top: 217px; height: 49px; width: 1200px; }
  .main-nav a {
    position: absolute; top: 12px; color: var(--white); text-decoration: none;
    font-size: 19px; font-weight: 300;
  }
  .brand {
    position: absolute; left: 100px; top: 70px; width: 240px;
    display: flex; align-items: center; gap: 12px;
  }
  .brand-dot { width: 54px; height: 54px; border-radius: 50%; background: #f4ead6; flex: none; }
  .brand-name { color: var(--white); font-size: 26px; font-weight: 600; line-height: 1.1; }
  .content-panel {
    position: absolute; left: 120px; top: 266px; width: 960px; height: 658px;
    background: var(--white); border-radius: 0 0 10px 10px;
  }
  .script-heading {
    position: absolute; font-family: "Kalam", cursive; color: var(--orange);
    font-weight: 400; font-size: 26px; line-height: 1; white-space: nowrap;
  }
  .ingredient-photo { position: absolute; border-radius: 40px; }
  .ingredient { position: absolute; width: 232px; }
  .ingredient h3 { color: var(--green); font-size: 17px; font-weight: 600; margin-bottom: 3px; }
  .ingredient p, .story p { font-size: 14px; line-height: 20px; font-weight: 300; }
  .story { position: absolute; left: 152px; top: 748px; width: 650px; }
  .story p + p { margin-top: 10px; }
  .menu-card {
    position: absolute; left: 833px; top: 701px; width: 220px; height: 189px;
    display: block; text-decoration: none;
    border-radius: 12px; overflow: hidden; background: var(--chalk);
  }
  .menu-board { height: 140px; background: linear-gradient(160deg, #3c3c3c, #1f1f1f); }
  .menu-label {
    height: 49px; background: var(--green); color: var(--white);
    font-family: "Kalam", cursive; font-size: 26px; text-align: center; line-height: 52px;
  }
  .site-footer { position: absolute; top: 944px; left: 147px; width: 901px; font-size: 12px; font-weight: 300; color: var(--white); }
  .site-footer .legal { position: absolute; right: 0; top: 0; }
</style>
</head>
<body>
  <div class="wood-backdrop" role="img" aria-label="Dunkle Holzdielen als Hintergrund"></div>
  <div class="hero-photo" role="img" aria-label="Nahaufnahme eines Burgers mit Salat, Tomate und Käse"></div>
  <div class="nav-band"></div>
  <nav class="main-nav">
    <a href="#" style="left:352px">Philosophie</a>
    <a href="#" style="left:502px">Zutaten</a>
    <a href="#" style="left:623px">Restaurant</a>
    <a href="#" style="left:763px">Team</a>
    <a href="#" style="left:861px">Kontakt</a>
  </nav>
  <div class="brand">
    <span class="brand-dot"></span>
    <span class="brand-name">1912 Zur Glutpfanne</span>
  </div>

  <main class="content-panel"></main>

  <h1 class="script-heading" style="left:342px;top:300px">Quit Fastfood – Frische Zutaten mit Liebe verarbeitet</h1>

  <div class="ingredient-photo" role="img" aria-label="Sesambrötchen" style="left:148px;top:358px;width:178px;height:106px;background:radial-gradient(ellipse at 50% 40%,#e3a35a,#b0631f)"></div>
  <section class="ingredient" style="left:343px;top:359px">
    <h3>Selbstgebackenes Brot</h3>
    <p>Lorem ipsum dolor sit amet, consetetur sadipscing elitr, sed diam nonumy eirmod tempor invidunt ut labore et dolore magna aliquyam.</p>
  </section>

  <div class="ingredient-photo" role="img" aria-label="Gegrilltes Rindfleisch-Patty" style="left:617px;top:372px;width:200px;height:92px;background:radial-gradient(ellipse at 50% 45%,#8a4a3a,#4b2418)"></div>
  <section class="ingredient" style="left:831px;top:359px">
    <h3>Frisches Bio-Rinderhack</h3>
    <p>Lorem ipsum dolor sit amet, consetetur sadipscing elitr, sed diam nonumy eirmod tempor invidunt ut labore et dolore magna aliquyam.</p>
  </section>

  <div class="ingredient-photo" role="img" aria-label="Stück Käse" style="left:152px;top:512px;width:166px;height:134px;border-radius:20px;background:linear-gradient(150deg,#fbe08a,#f0b830)"></div>
  <section class="ingredient" style="left:343px;top:516px">
    <h3>Käse aus Familienbetrieb</h3>
    <p>Lorem ipsum dolor sit amet, consetetur sadipscing elitr, sed diam nonumy eirmod tempor invidunt ut labore et dolore magna aliquyam.</p>
  </section>

  <div class="ingredient-photo" role="img" aria-label="Flaschen mit Tomatensauce und frische Tomaten" style="left:615px;top:505px;width:196px;height:116px;border-radius:20px;background:radial-gradient(ellipse at 50% 70%,#e0281c,#f7d6d2)"></div>
  <section class="ingredient" style="left:831px;top:516px">
    <h3>Hausgemachte Saucen</h3>
    <p>Lorem ipsum dolor sit amet, consetetur sadipscing elitr, sed diam nonumy eirmod tempor invidunt ut labore et dolore magna aliquyam.</p>
  </section>

  <h2 class="script-heading" style="left:150px;top:704px;font-size:27px">Qualität, die man schmeckt!</h2>
  <section class="story">
    <p>Lorem ipsum dolor sit amet, consetetur sadipscing elitr, sed diam nonumy eirmod tempor invidunt ut labore et dolore magna aliquyam erat, sed diam voluptua. At vero eos et accusam et justo duo dolores et ea rebum. Stet clita kasd gubergren, no sea takimata sanctus est Lorem ipsum dolor sit amet. Lorem ipsum dolor sit amet, consetetur sadipscing elitr, sed diam nonumy eirmod tempor invidunt ut labore et dolore magna.</p>
    <p>At vero eos et accusam et justo duo dolores et ea rebum. Stet clita kasd gubergren, sed diam nonumy eirmod tem no sea takimata sanctus est Lorem ipsum dolor sit amet.</p>
  </section>

  <a class="menu-card" href="#">
    <div class="menu-board" role="img" aria-label="Kreidetafel mit der Burger-Speisekarte"></div>
    <div class="menu-label">Speisekarte</div>
  </a>

  <footer class="site-footer">
    <span>(C) 2014 - Zur Glutpfanne</span>
    <span class="legal">Anfahrt &nbsp;|&nbsp; Impressum</span>
  </footer>
</body>
</html>
```